Coffee House With Cycling Theme Wants Business Cards

We want to create a business card for a coffee house that has a cycling theme. We expect to use the current logo on one side of the business card and we have been considering adding the words 'COFFEE HOUSE' underneath (see example). For the other side of the business card we want an interesting design with tag-line, address and social media links (the normal business card stuff). See examples provided but we are not fixed on having it exactly as shown, we are very open to great creative ideas. Please note our logo has the initials ‘RM' in orange embedded in the design and this must be retained. However, you can play with the words COFFEE HOUSE as well as use the orange color on the backside of the business card, as you see fit. For an image on the backside of the business card it can be a photo, hand-drawn or whatever but it must visually combine coffee and cycling in some way. The interior of the Coffee House will be reclaimed wood, rustic and have an urban feel to it with cycling artifacts hanging from the walls/ceiling, etc. Finally, it would be beneficial if the business card design elements can be easily used on flyers and other promotional assets. Good luck, we are looking forward to seeing your creative ideas.

Target Market(s)

Coffee lovers and cycling fans

Contact Information for Business Card

See project description.

Colors

Designer to choose colors to be used in the design.

Requirements
Must have
• Must use the current logo provided and combine a coffee and bike theme.
Nice to have
• Orange is used in current logo and could be used as an accent color on the backside of the business card.

```html
<!DOCTYPE html>
<html lang="en">
<head>
<meta charset="utf-8">
<title>RM Coffee House – Business Cards</title>
<link rel="stylesheet" href="https://fonts.googleapis.com/css2?family=Work+Sans:wght@400;500;600&display=swap">
<style>
  :root {
    --page: #161616;
    --card: #232323;
    --card-edge: #2b2b2b;
    --emboss: #8a8a8a;
    --orange: #f0682a;
    --white: #ffffff;
    --soft-white: #e9e9e9;
  }
  html, body {
    margin: 0;
    padding: 0;
    width: 1200px;
    height: 900px;
    overflow: hidden;
    background: var(--page);
  }
  .canvas {
    position: relative;
    width: 1200px;
    height: 900px;
  }
  .card {
    position: absolute;
    left: 250px;
    width: 700px;
    height: 400px;
    background: linear-gradient(135deg, var(--card-edge), var(--card));
    box-sizing: border-box;
    overflow: hidden;
  }
  .card--front { top: 30px; }
  .card--back  { top: 460px; }

  .brand {
    display: flex;
    align-items: center;
    gap: 14px;
    font-family: "Work Sans", sans-serif;
    font-weight: 500;
    white-space: nowrap;
  }
  .brand .mark-dot {
    width: 22px;
    height: 22px;
    border-radius: 50%;
    background: currentColor;
    flex: none;
  }

  /* front */
  .front-brand {
    position: absolute;
    left: 0; right: 0; top: 172px;
    justify-content: center;
    font-size: 44px;
    color: var(--emboss);
  }

  /* back */
  .back-brand {
    position: absolute;
    left: 36px; top: 138px;
    font-size: 32px;
    color: var(--orange);
  }
  .back-brand .mark-dot { width: 18px; height: 18px; }
  .divider {
    position: absolute;
    left: 392px; top: 60px;
    width: 2px; height: 200px;
    background: var(--soft-white);
  }
  .contact {
    position: absolute;
    left: 420px; top: 62px;
    font-family: "Work Sans", sans-serif;
    color: var(--white);
    font-size: 16px;
    line-height: 1.45;
  }
  .contact .name {
    margin: 0;
    font-size: 24px;
    font-weight: 600;
    letter-spacing: 2px;
    color: var(--orange);
  }
  .contact .role {
    margin: 0 0 14px;
    font-size: 16px;
  }
  .contact .address { margin: 0 0 10px; }
  .contact-list { list-style: none; margin: 0; padding: 0; }
  .contact-list li { display: flex; align-items: center; gap: 8px; }
  .contact-list svg { width: 12px; height: 12px; flex: none; }
  .social {
    position: absolute;
    left: 0; right: 0; bottom: 40px;
    display: flex;
    justify-content: center;
    gap: 50px;
    font-family: "Work Sans", sans-serif;
    font-size: 19px;
    color: var(--white);
  }
  .social span { display: flex; align-items: center; gap: 12px; }
  .social .dot {
    width: 18px; height: 18px;
    background: var(--orange);
  }
</style>
</head>
<body>
<div class="canvas">

  <section class="card card--front" aria-label="Card front">
    <div class="brand front-brand">
      <i class="mark-dot" aria-hidden="true"></i>
      <span>RM Coffee House</span>
    </div>
  </section>

  <section class="card card--back" aria-label="Card back">
    <div class="brand back-brand">
      <i class="mark-dot" aria-hidden="true"></i>
      <span>RM Coffee House</span>
    </div>

    <div class="divider"></div>

    <div class="contact">
      <p class="name">DANIEL HART</p>
      <p class="role">Director</p>
      <p class="address">58b Harbour Lane,<br>Lyttelton, NZ, 8082</p>
      <ul class="contact-list">
        <li>
          <svg viewBox="0 0 12 12" aria-hidden="true"><path d="M3 1 L5 3 L4 5 Q5 7 7 8 L9 7 L11 9 L9.5 11 Q4 10 1 3 Z" fill="none" stroke="var(--orange)" stroke-width="1.2"/></svg>
          (555) 014-2290
        </li>
        <li>
          <svg viewBox="0 0 12 12" aria-hidden="true"><rect x="1" y="2.5" width="10" height="7" fill="none" stroke="var(--orange)" stroke-width="1.2"/><path d="M1 2.5 L6 6.5 L11 2.5" fill="none" stroke="var(--orange)" stroke-width="1.2"/></svg>
          info@rmcoffeehouse.com
        </li>
        <li>
          <svg viewBox="0 0 12 12" aria-hidden="true"><circle cx="6" cy="6" r="5" fill="none" stroke="var(--orange)" stroke-width="1.2"/><ellipse cx="6" cy="6" rx="2.2" ry="5" fill="none" stroke="var(--orange)" stroke-width="1"/><path d="M1 6 H11" stroke="var(--orange)" stroke-width="1"/></svg>
          www.rmcoffeehouse.com
        </li>
      </ul>
    </div>

    <div class="social">
      <span><i class="dot"></i>rmcoffeehouse.com</span>
      <span><i class="dot"></i>rmcoffeehouse.com</span>
    </div>
  </section>

</div>
</body>
</html>
```